website for local kavenda practicioner and yoga teacher trainer

The website should function primarily as:
A place where people can discover Kavenda and book sessions.
A central hub connecting all of my work.
A professional home that reflects my personality and approach.
Website design for Liesbet Oonwerk — Kavenda® Structural Integration practitioner, movement educator, yoga teacher and teacher trainer.
A website that can grow with future projects.
The website should feel: Warm, Human, Invitational, Professional, Accessible, Intelligent, Calm, Clear, Playful, Exploratory, Trustworthy
Avoid: New age aesthetics, Mystical clichés, Excessive spirituality, ”Guru" vibes, Overly clinical design, Corporate wellness branding, Busy layouts
Think: modern, grounded, curious and real.
My work combines three interconnected areas:
1.Bodywork: Touch, structure, awareness and one-on-one support.
2. Movement: Yoga, Pilates and embodied movement.
3. Education: Teacher trainings, workshops and continued learning.
Underlying values:
Curiosity over certainty
Possibility over perfection
Complexity without overwhelm
Science and lived experience together
Exploration rather than dogma
Human beings before methods
The primary goal of the website is to introduce people to Kavenda® Structural Integration and make it easy for them to:
Understand what Kavenda is
Discover whether it might be relevant for them
Learn what to expect from a session
Book an appointment
Booking should always feel visible and easy.
Secondary Goal: Present all other aspects of my work in one coherent place:
Yoga classes
Pilates classes
Teacher trainings
Workshops
Retreats
One-on-one movement sessions
Collaborations with studios
Website Structure
1: HOME
1.1.Hero Section: Large welcoming image
1.2 Two Main Pathways
- Bodywork: Kavenda® Structural Integration
- Movement & Education: Yoga, Pilates, trainings, workshops and retreats
- About Preview: Small introduction with portrait. + Button:
Read More
1.3 Current Events / What's Coming Up: Upcoming trainings, workshops and retreats. (This section should be easy to update)
1.4. Contact / Newsletter: Simple contact information
2: Kavenda® Structural Integration
What is Kavenda?
For whom is it?
What does a session look like?
FAQ
Prices
Booking
Future possibility:
Kaven Movement sessions
3: Movement
- Introductory text.
- Studio Classes (link to “my home base” - > local yoga studio)
- One-to-One Sessions: booking option (this is small; not a key aspect I want to promote)
- Workshops/ Retreats / Teacher Trainings => This section should be flexible and easy to update. Visitors should be able to click into specific offerings.
4. Events
Dynamic page for: Teacher trainings, Retreats, Workshops (see section in movement; here more elaborate)
Each event should contain: Image, Short description, Location, Date, Button for more information. (Linking to hosting studio/location)
5. Work With Me
For studios, organisations and teacher training schools.
Examples: Guest teaching, Workshops, Anatomy, Sequencing, Teacher development , Continuing education -> Clear call-to-action.
Call to action!!=> Book a Session
Prominent button in the navigation.
Footer:
- About Me: Longer biography (6th page)
Personal story and background.
- Testimonials (7th page): Separate page containing testimonials from:
Kavenda clients
Students
Teacher trainees
- Contact: 8th page
Visual Direction
Natural textures. Lots of white space.Editorial feeling.Professional photography.Simple navigation.
Less "wellness influencer.” More:Thoughtful, Contemporary, Timeless, Grounded, Human
Photography should show:
Teaching
Hands-on work
Natural movement
Real interaction
Simplicity
Avoid stereotypical yoga imagery and overly spiritual aesthetics.
Keywords
Warm. Curious. Human. Professional. Embodied. Intelligent. Accessible. Playful. Grounded. Exploratory. Real.
Inspiration / Core Message
Helping people feel more at home in their bodies through touch, movement and education.
The website should communicate that these are not separate services, but different expressions of the same intention:
Bodywork • Movement • Education.
Colours:
light orange/beige: e3d5c4
light orange/off white: f9f7f3
gray azure: 556b78
orange: d07b5a
grey orange: c09f80
dark grey: 3e3e3e
dark gray cyan 2f4f4f
gray green colour: a7c4a0
Fonts: Montserrat and Poppins + raleway
In added documents a try out idea of a website + logo. I will mainly use the logo with diffrent colours (image next to text).
My audience consists of people who want to feel more at home in their bodies and who appreciate a thoughtful, grounded and human approach to movement, touch and education. (30-65yo)
wellbeing
5+ page
- montserrat, poppins, raleway

```html
<!DOCTYPE html>
<html lang="en">
<head>
<meta charset="utf-8">
<title>Movement &amp; Education — Liesbet Oonwerk</title>
<link href="https://fonts.googleapis.com/css2?family=Raleway:wght@300;400;500;600&family=Poppins:wght@300;400;500;600&family=Montserrat:wght@500;600;700&display=swap" rel="stylesheet">
<style>
:root{
  --sand:#e3d5c4;
  --offwhite:#f9f7f3;
  --white:#ffffff;
  --orange:#d07b5a;
  --greyorange:#c09f80;
  --dark:#3e3e3e;
  --text:#3e3e3e;
  --muted:#b9b4ae;
}
*{margin:0;padding:0;box-sizing:border-box}
html,body{width:1200px;height:2836px;overflow:hidden}
body{position:relative;background:var(--white);font-family:'Poppins',sans-serif;color:var(--text)}
.abs{position:absolute}
a{text-decoration:none;color:inherit}

/* header */
.hero{left:0;top:0;width:1200px;height:470px;background:var(--offwhite);overflow:hidden}
.hero-photo{position:absolute;left:0;top:0;width:1200px;height:470px}
.brand{left:91px;top:22px;color:var(--white)}
.brand-name{font-family:'Poppins',sans-serif;font-size:16px;font-weight:500;line-height:20px}
.brand-tag{font-family:'Montserrat',sans-serif;font-size:7.5px;font-weight:600;letter-spacing:.6px;opacity:.85}
.nav{right:243px;top:28px;display:flex;gap:19px;font-size:12px;color:var(--white);white-space:nowrap}
.nav .current{color:var(--orange)}
.btn-book{left:982px;top:18px;width:127px;height:37px;border-radius:19px;background:var(--orange);color:var(--white);font-size:12px;display:flex;align-items:center;justify-content:center}
.crumb{left:91px;top:127px;font-family:'Montserrat',sans-serif;font-weight:600;font-size:15px;letter-spacing:2.4px;color:rgba(255,255,255,.85)}
.hero-title{left:90px;top:170px;font-family:'Raleway',sans-serif;font-weight:300;font-size:70px;line-height:74px;color:var(--white)}
.hero-sub{left:91px;top:339px;width:480px;font-size:16px;line-height:26px;color:var(--white)}

.eyebrow{font-family:'Montserrat',sans-serif;font-weight:600;font-size:9.5px;letter-spacing:3px;color:var(--orange);text-transform:uppercase}
.h2{font-family:'Raleway',sans-serif;font-weight:300;font-size:48px;line-height:54px;color:var(--text)}
.body{font-size:14.5px;line-height:24px}

/* intro */
.intro{left:269px;top:560px;width:680px}
.intro .h2{margin-top:10px}
.intro p{margin-bottom:14px}

/* studio */
.studio{left:0;top:903px;width:1200px;height:551px;background:var(--offwhite)}
.studio-photo{position:absolute;left:145px;top:89px;width:374px;height:374px;border-radius:50%;background:radial-gradient(circle at 40% 30%,#d9dfe0 0%,#9fb0b0 35%,#4f6456 65%,#35452f 100%);box-shadow:0 14px 30px rgba(0,0,0,.12)}
.studio-text{position:absolute;left:627px;top:185px;width:470px}
.studio-text .h2{margin:10px 0 2px}
.btn-dark{display:inline-flex;align-items:center;justify-content:center;background:var(--dark);color:var(--white);font-size:12.5px;font-weight:500;border-radius:24px}
.studio-text .btn-dark{margin-top:14px;width:177px;height:46px}

/* one to one */
.personal{left:0;top:1545px;width:1200px;text-align:center}
.personal .h2{margin:10px 0 2px}
.personal .body{width:440px;margin:0 auto}
.personal .link{display:block;margin-top:18px;font-size:13px;color:var(--orange)}

/* events */
.events{left:0;top:1802px;width:1200px;height:760px;background:var(--sand)}
.events .eyebrow{position:absolute;left:91px;top:92px}
.events .h2{position:absolute;left:89px;top:118px}
.arrow{position:absolute;top:108px;width:40px;height:40px;border-radius:50%;display:flex;align-items:center;justify-content:center}
.arrow.prev{left:1016px;background:rgba(255,255,255,.4)}
.arrow.next{left:1068px;background:var(--white)}
.event{position:absolute;top:199px;width:325px;height:325px;border-radius:50%;display:flex;flex-direction:column;align-items:center;justify-content:center;color:var(--white);text-align:center}
.event-title{font-size:13px;font-weight:500}
.event-meta{font-size:10.5px}
.e1{left:91px;background:radial-gradient(circle at 50% 30%,#d9a277 0%,#8a5538 45%,#3a2419 100%)}
.e2{left:438px;background:radial-gradient(circle at 50% 25%,#b9895c 0%,#6e4c32 45%,#2f2520 100%)}
.e3{left:785px;background:linear-gradient(180deg,#c5ccd2 0%,#a9b2b8 50%,#b9ab98 80%,#8d8476 100%)}
.events .btn-dark{position:absolute;left:548px;top:553px;width:104px;height:45px}

/* footer */
.footer-curve{left:0;top:2487px;width:1200px;height:349px}
.footer-col{top:2566px;font-size:12px;color:var(--muted)}
.footer-col h4{font-size:13px;font-weight:500;color:var(--white);margin-bottom:14px}
.footer-col li{list-style:none;line-height:26px}
.footer-col .tag{margin-bottom:20px}
.copyright{left:0;top:2800px;width:1200px;text-align:center;font-size:9.5px;color:#8c8884}
</style>
</head>
<body>

<header class="hero abs">
  <svg class="hero-photo" viewBox="0 0 1200 470" role="img" aria-label="Photo of a person resting in child's pose on a yoga mat on a wooden floor">
    <defs>
      <linearGradient id="heroTone" x1="0" y1="0" x2="1" y2="0.4">
        <stop offset="0" stop-color="#4a4538"/>
        <stop offset="0.45" stop-color="#3d3e33"/>
        <stop offset="0.75" stop-color="#7a5a3e"/>
        <stop offset="1" stop-color="#9c7048"/>
      </linearGradient>
      <linearGradient id="heroShade" x1="0" y1="0" x2="1" y2="0">
        <stop offset="0" stop-color="#000" stop-opacity=".35"/>
        <stop offset="0.6" stop-color="#000" stop-opacity=".05"/>
        <stop offset="1" stop-color="#000" stop-opacity="0"/>
      </linearGradient>
    </defs>
    <path d="M0 0H1200V380Q600 560 0 380Z" fill="url(#heroTone)"/>
    <path d="M0 0H1200V380Q600 560 0 380Z" fill="url(#heroShade)"/>
  </svg>

  <div class="brand abs">
    <div class="brand-name">Liesbet Oonwerk</div>
    <div class="brand-tag">Kavenda® Structural Integration</div>
  </div>
  <nav class="nav abs">
    <a>Home</a><a>Kavenda</a><a class="current">Movement</a><a>Events</a><a>Work With Me</a><a>About</a><a>Testimonials</a><a>Contact</a>
  </nav>
  <a class="btn-book abs">Book a Session</a>

  <div class="crumb abs">HOME / MOVEMENT</div>
  <h1 class="hero-title abs">Movement &amp;<br>Education</h1>
  <p class="hero-sub abs">Yoga, Pilates, workshops and teacher trainings — grounded,<br>intelligent and embodied.</p>
</header>

<section class="intro abs">
  <div class="eyebrow">Movement</div>
  <h2 class="h2">Moving with curiosity, not<br>control</h2>
  <p class="body">Movement is not about performing or perfecting poses. It’s about discovering how your body<br>wants to move, and finding joy, freedom and intelligence in that exploration.</p>
  <p class="body">My classes blend yoga, Pilates and embodied movement science. Accessible, thoughtful and<br>playful. All levels welcome.</p>
</section>

<section class="studio abs">
  <div class="studio-photo" role="img" aria-label="Photo of a person in tree pose on a misty green mountain ridge"></div>
  <div class="studio-text">
    <div class="eyebrow">Studio Classes</div>
    <h2 class="h2">My home base</h2>
    <p class="body">I teach regularly at <strong>Linden Yoga Studio</strong>. Classes include gentle vinyasa, embodied flow and Pilates-inspired movement.</p>
    <a class="btn-dark">Visit Studio Website</a>
  </div>
</section>

<section class="personal abs">
  <div class="eyebrow">One-to-one sessions</div>
  <h2 class="h2">Personal movement guidance</h2>
  <p class="body">Tailored to your body, your goals and your curiosity. Breath, alignment, functional movement.</p>
  <a class="link">Inquire about sessions</a>
</section>

<section class="events abs">
  <div class="eyebrow">Workshops &amp; Retreats</div>
  <h2 class="h2">Immersions &amp; Intensives</h2>
  <a class="arrow prev" aria-label="Previous"><svg width="18" height="10" viewBox="0 0 18 10"><path d="M17 5H1M5 1L1 5l4 4" fill="none" stroke="#c9b9a6" stroke-width="1.3"/></svg></a>
  <a class="arrow next" aria-label="Next"><svg width="18" height="10" viewBox="0 0 18 10"><path d="M1 5h16M13 1l4 4-4 4" fill="none" stroke="#3e3e3e" stroke-width="1.3"/></svg></a>

  <a class="event e1" role="img" aria-label="Photo of a person meditating at sunset in a wooden pavilion">
    <span class="event-title">Embodied Anatomy</span><span class="event-meta">Jun 24–28 · Antwerp</span>
  </a>
  <a class="event e2" role="img" aria-label="Photo of a group practising yoga in a warm-lit studio">
    <span class="event-title">YTT Module 1</span><span class="event-meta">Sep 12–14 · Brussels</span>
  </a>
  <a class="event e3" role="img" aria-label="Photo of a group in tree pose on a beach">
    <span class="event-title">Autumn Retreat</span><span class="event-meta">Oct 5–10 · Portugal</span>
  </a>

  <a class="btn-dark">View all</a>
</section>

<footer>
  <svg class="footer-curve abs" viewBox="0 0 1200 349" aria-hidden="true">
    <path d="M0 56Q600 -56 1200 56V349H0Z" fill="var(--dark)"/>
  </svg>
  <div class="footer-col abs" style="left:91px">
    <h4>Liesbet Oonwerk</h4>
    <p class="tag">Kavenda® · Movement · Education</p>
    <p>Helping people feel more at home in their bodies.</p>
  </div>
  <div class="footer-col abs" style="left:489px">
    <h4>Explore</h4>
    <ul><li>Kavenda</li><li>Movement</li><li>Events</li><li>Work With Me</li></ul>
  </div>
  <div class="footer-col abs" style="left:710px">
    <h4>About</h4>
    <ul><li>About Me</li><li>Testimonials</li><li>Contact</li></ul>
  </div>
  <div class="footer-col abs" style="left:930px">
    <h4>Connect</h4>
    <ul><li>Instagram</li><li>Facebook</li><li>LinkedIn</li><li>Email</li></ul>
  </div>
  <p class="copyright abs">© 2026 Liesbet Oonwerk. All rights reserved.</p>
</footer>

</body>
</html>
```